Attorney Website Design

I need a top quality attorney website layout designed. Here are some examples of what I feel are great websites:
http://www.brelmoradivorceattorney.example/
http://www.vethomirlawfirm.example/
http://www.plexfirm.example/
http://www.harrowgatecriminaldefensefirm.example/
http://www.qzfirm.example/
http://www.tolvermoorcriminaldefensefirm.example/
http://www.drennocriminalattorneys.example/
http://www.qzfirm.example/
What we like about these sites:
• The different layers
• Subtle designs, textures, curves
• 3 dimensional
• Floating effects
• Prominent phone number
• Location of Areas of Practice
• Request A Consultation Prominent
• Right side bar with practice areas
• Badges
• Clear Calls to Action
• Dynamic/Staying Top navigation when you scroll
The project will be for a home page and then also an interior page (should be similar to home page).
I want to make it understood I am looking for a design which is not a typical "template" site which I can find anywhere for $50. This budget and project is for a "Custom" website design. Please submit designs similar in quality to the samples links I have posted. Creativity is a MUST! The best way to explain this is, I want a design that I can feel it unique and original, not something that looks like 95% of all websites out there.
Owen
I just wanted everyone to know that so far I am not to pleased with any of the designs. I am not looking for cut/pasting of other peoples websites but ORIGINAL and CREATIVE work.
Industry/Entity Type
Attorney

```html
<!DOCTYPE html>
<html lang="en">
<head>
<meta charset="utf-8">
<title>Halvard Law Firm</title>
<link href="https://fonts.googleapis.com/css2?family=Lato:wght@300;400;700&family=Libre+Baskerville:ital@0;1&display=swap" rel="stylesheet">
<style>
:root{
  --black:#060606;
  --header:#0b0b0b;
  --yellow:#ffe400;
  --dark:#2c3035;
  --light:#ebebeb;
  --text-grey:#7a7a7a;
  --muted:#8d9096;
  --white:#ffffff;
  --line:#4a4e54;
  --field:#f2f2f2;
}
*{box-sizing:border-box;margin:0;padding:0}
html,body{width:1200px;height:2880px;overflow:hidden}
body{position:relative;background:var(--black);font-family:'Lato',sans-serif;color:var(--white)}
.abs{position:absolute}
section,header,footer{position:absolute;left:0;width:1200px}

/* header + hero */
.site-header{top:0;height:703px;background:var(--header);border-top:4px solid var(--yellow)}
.cta-tab{left:850px;top:0;width:254px;height:34px;background:var(--yellow);color:#111;font-weight:700;font-size:15px;text-align:center;line-height:32px;border-radius:0 0 4px 4px;letter-spacing:.5px}
.logo-box{left:102px;top:0;width:190px;height:170px;background:linear-gradient(#2b2b2b,#1a1a1a);display:flex;align-items:center;justify-content:center;gap:10px}
.logo-box .mark{width:14px;height:14px;background:var(--white);border-radius:50%}
.logo-box .name{font-family:'Libre Baskerville',serif;font-size:30px;color:var(--white)}
.call{right:148px;top:64px;font-size:19px;color:var(--white)}
.call-icon{left:1066px;top:60px;width:38px;height:38px;background:var(--yellow);display:flex;align-items:center;justify-content:center}
.main-nav{top:126px;left:0;width:1200px;height:46px}
.main-nav a{position:absolute;top:0;font-size:18px;color:var(--white);text-decoration:none}
.main-nav a.active{color:var(--yellow)}
.nav-underline{left:417px;top:169px;width:63px;height:6px;background:var(--yellow)}
.nav-rule{left:102px;top:171px;width:1002px;height:1px;background:#262626}
.hero-title{left:170px;top:305px;width:360px;text-align:center;font-family:'Libre Baskerville',serif;font-style:italic;font-size:25px;line-height:34px;text-transform:uppercase;letter-spacing:1px}
.hero-copy{left:169px;top:392px;width:354px;text-align:center;font-size:13.5px;line-height:18px;color:#9b9b9b}
.btn-yellow{background:var(--yellow);color:#111;font-weight:700;text-align:center}
.hero-btn{left:263px;top:518px;width:175px;height:48px;line-height:48px;font-size:15px}
.hero-photo{left:595px;top:172px;width:530px;height:475px;background:radial-gradient(ellipse at 60% 40%,#3a3a3c,#121212 70%)}
.hero-arrow{top:372px;width:42px;height:42px;border:2px solid #8a8a8a;border-radius:50%;display:flex;align-items:center;justify-content:center}
.hero-dots{left:563px;top:662px;display:flex;gap:6px}
.hero-dots span{width:9px;height:9px;border-radius:50%;background:#6b6b6b}
.hero-dots span.on{background:var(--yellow);box-shadow:0 0 0 2px #444}

/* about */
.about{top:703px;height:305px;background:var(--light);color:#333}
.section-title{font-size:22px;font-weight:400}
.about .section-title{left:102px;top:40px;color:#222}
.about p{position:absolute;left:102px;width:635px;font-size:12.5px;line-height:19px;color:var(--text-grey)}
.btn-dark{left:637px;top:259px;width:100px;height:21px;background:#111;color:var(--white);font-size:11px;text-align:center;line-height:21px}
.video{left:789px;top:46px;width:311px;height:232px;background:linear-gradient(160deg,#6a3a1c,#c98a45 55%,#3a1f0e);display:flex;align-items:center;justify-content:center}
.play{width:60px;height:42px;background:#cc1f1f;border-radius:10px;display:flex;align-items:center;justify-content:center}

/* attorneys */
.attorneys{top:1008px;height:534px;background:var(--dark)}
.attorneys .section-title{left:102px;top:34px}
.subtitle{left:102px;top:64px;font-size:14px;color:#5e636a}
.attorney{top:111px;width:188px}
.attorney .photo{width:188px;height:210px;background:linear-gradient(#c9c9c9,#6f7277)}
.attorney .nm{margin-top:12px;text-align:center;font-size:14px}
.attorney .role{text-align:center;font-size:10px;color:#c9c9c9}
.att-rule{left:102px;top:376px;width:635px;height:1px;background:#65696f}
.badges-title{left:102px;top:396px;font-size:22px}
.badge{top:436px;height:54px;background:#e8e8e8}
.sidebar{left:787px;top:29px;width:311px;height:461px;background:linear-gradient(#f2f2f2,#d8d8d8);border-radius:6px;overflow:hidden;border:1px solid #bcbcbc}
.sidebar h3{height:54px;line-height:54px;background:#101010;color:var(--white);text-align:center;font-size:17px;font-weight:400;border-radius:6px 6px 0 0}
.sidebar ul{list-style:none;padding:10px 0 0 16px}
.sidebar li{width:240px;height:29px;line-height:28px;font-size:12.5px;color:#8a8a8a;border-bottom:1px solid #cfcfcf;padding-left:12px;position:relative}
.sidebar li:before{content:"›";position:absolute;left:0;color:#aaa}

/* testimonials */
.testimonials{top:1542px;height:336px;background:var(--light);color:#222}
.testimonials .section-title{left:0;width:1200px;text-align:center;top:55px}
.testi{top:113px;width:340px}
.avatar{position:absolute;left:0;top:0;width:69px;height:69px;border-radius:50%;background:linear-gradient(#d8d8d8,#9d9d9d);border:4px solid #fff;box-shadow:0 0 0 1px #ddd}
.quote-mark{position:absolute;left:100px;top:-6px;font-family:'Libre Baskerville',serif;font-size:60px;color:#c9c9c9;line-height:60px}
.quote{position:absolute;left:100px;top:24px;width:236px;font-family:'Libre Baskerville',serif;font-size:12px;line-height:19px;color:#333;text-align:justify;text-indent:44px}
.t-name{position:absolute;left:100px;top:98px;font-family:'Libre Baskerville',serif;font-size:12px;color:#222}
.t-role{position:absolute;left:100px;top:118px;font-size:9px;color:#999}
.t-role b{color:#3b7fd1;font-weight:400}
.t-dots{left:584px;top:276px;display:flex;gap:5px}
.t-dots span{width:6px;height:6px;border-radius:50%;background:#bbb}
.t-dots span.on{background:#222}

/* location + form */
.contact-band{top:1878px;height:585px;background:var(--dark)}
.contact-band .section-title{top:40px}
.map{left:102px;top:102px;width:635px;height:443px;background:linear-gradient(135deg,#eeece6,#dedbd2)}
.map-card{left:413px;top:140px;width:261px;height:184px;background:#1b1d20;border-radius:10px;padding:22px 20px}
.map-card h4{font-size:20px;font-weight:400;margin-bottom:14px}
.map-card p{font-size:12.5px;line-height:19px;display:flex;gap:8px;align-items:flex-start}
.form-label{left:785px;font-size:14px;color:#9aa0a7}
.field{left:785px;width:315px;background:var(--field);border-radius:2px}
.submit{left:1002px;top:499px;width:98px;height:44px;line-height:44px;border-radius:4px;font-size:16px;font-weight:400}

/* footer */
.site-footer{top:2463px;height:417px;background:var(--black)}
.f-head{top:62px;font-size:17px;color:var(--yellow)}
.f-links{top:106px;list-style:none;width:255px}
.f-links li{height:33px;line-height:32px;font-size:13px;color:#7d7d7d;border-bottom:1px solid #1c1c1c;padding-left:14px;position:relative}
.f-links li:before{content:"›";position:absolute;left:0;color:#555}
.thumb{width:58px;height:58px;background:linear-gradient(#cfc6bd,#7a6d62)}
.f-contact{left:954px;top:100px;font-size:12px;line-height:19px;color:#8a8a8a}
.f-contact p{display:flex;gap:8px;align-items:flex-start}
.dash{left:0;top:2778px;width:1200px;border-top:2px dashed #3a3a3a;position:absolute}
.social{top:355px;width:38px;height:38px;border:2px solid #4a4a4a;border-radius:50%}
.copy{left:0;width:1200px;text-align:center;top:394px;font-size:10px;color:#777}
.copy b{color:var(--yellow);font-weight:400}
</style>
</head>
<body>

<header class="site-header">
  <div class="abs cta-tab">CALL TO ACTION</div>
  <div class="abs logo-box"><span class="mark"></span><span class="name">Halvard</span></div>
  <div class="abs call">Call us - 555-201-7734</div>
  <div class="abs call-icon">
    <svg width="20" height="20" viewBox="0 0 24 24"><path fill="#111" d="M6.6 10.8a15 15 0 0 0 6.6 6.6l2.2-2.2a1 1 0 0 1 1-.25 11.4 11.4 0 0 0 3.6.57 1 1 0 0 1 1 1V20a1 1 0 0 1-1 1A17 17 0 0 1 3 4a1 1 0 0 1 1-1h3.5a1 1 0 0 1 1 1c0 1.25.2 2.45.57 3.57a1 1 0 0 1-.25 1z"/></svg>
  </div>
  <nav class="abs main-nav">
    <a class="active" style="left:430px">Home</a>
    <a style="left:503px">About</a>
    <a style="left:574px">Practice Area</a>
    <a style="left:698px">Blog +</a>
    <a style="left:772px">Testimonial</a>
    <a style="left:881px">Free Consultation</a>
    <a style="left:1040px">Contact</a>
  </nav>
  <div class="abs nav-rule"></div>
  <div class="abs nav-underline"></div>

  <div class="abs hero-photo" role="img" aria-label="Photo of a confident attorney in a dark suit giving a thumbs up"></div>
  <h1 class="abs hero-title">Lorem ipsum<br>amet, consectetur</h1>
  <p class="abs hero-copy">Mauris laoreet nec justo eu semper. Suspendisse tempus dignissim augue, ut bibendum odio lobortis sit amet. Curabitur ornare placerat volutpat. Integer quis porta nunc, eu pretium ante. Vestibulum in sem eros. Duis scelerisque ultricies elit vitae rutrum.</p>
  <div class="abs btn-yellow hero-btn">READ MORE</div>
  <div class="abs hero-arrow" style="left:42px"><svg width="14" height="14" viewBox="0 0 14 14"><path d="M9 2 4 7l5 5" stroke="#aaa" stroke-width="2" fill="none"/></svg></div>
  <div class="abs hero-arrow" style="left:1121px"><svg width="14" height="14" viewBox="0 0 14 14"><path d="M5 2l5 5-5 5" stroke="#aaa" stroke-width="2" fill="none"/></svg></div>
  <div class="abs hero-dots"><span class="on"></span><span></span><span></span><span></span></div>
</header>

<section class="about">
  <h2 class="abs section-title">About Us</h2>
  <p style="top:80px">Lorem ipsum dolor sit amet, consectetur adipiscing elit. Proin tincidunt ullamcorper velit, et euismod dui ornare nec. Donec sagittis vestibulum nibh, et porttitor lectus pretium a. Maecenas a facilisis lectus. Nunc fermentum diam in bibendum feugiat. Proin sit amet nisi placerat, venenatis quam eu, luctus tellus. Sed nec fringilla justo. Duis ac fermentum ipsum, vel tempus quam. Phasellus eget enim libero.</p>
  <p style="top:178px">Early on, Sam and Joel recognized the trend of many distributors to consolidate purchases. They addressed this trend by broadening the product offering. They added fastening devices and anchors, electrical fittings, petroleum products (tapes, mastic &amp; cutting oil), tools and specialty items. As a result, business began to grow.</p>
  <div class="abs btn-dark">Read More</div>
  <div class="abs video" role="img" aria-label="Video still of brass scales of justice">
    <div class="play"><svg width="18" height="20" viewBox="0 0 18 20"><path d="M2 1l15 9-15 9z" fill="#fff"/></svg></div>
  </div>
</section>

<section class="attorneys">
  <h2 class="abs section-title">Meet Our Attorneys</h2>
  <div class="abs subtitle">The great team behind the successfull Management</div>
  <div class="abs attorney" style="left:102px"><div class="photo" role="img" aria-label="Portrait of attorney John Doe"></div><div class="nm">John Doe</div><div class="role">lorem ipsum dolor</div></div>
  <div class="abs attorney" style="left:324px"><div class="photo" role="img" aria-label="Portrait of attorney Ann Mary"></div><div class="nm">Ann Mary</div><div class="role">Sit amet dolor sit</div></div>
  <div class="abs attorney" style="left:547px"><div class="photo" role="img" aria-label="Portrait of attorney Marcus Ellery"></div><div class="nm">Marcus Ellery</div><div class="role">Contantry popular sit</div></div>
  <div class="abs att-rule"></div>
  <h3 class="abs badges-title" style="font-weight:400">Our Badges</h3>
  <div class="abs badge" style="left:102px;width:112px;border-radius:4px"></div>
  <div class="abs badge" style="left:278px;width:96px;border-radius:4px"></div>
  <div class="abs badge" style="left:428px;width:56px;border-radius:50%"></div>
  <div class="abs badge" style="left:558px;width:56px;border-radius:50%"></div>
  <div class="abs badge" style="left:672px;width:84px;height:34px;top:446px;border-radius:4px"></div>

  <aside class="abs sidebar">
    <h3>Practice Areas</h3>
    <ul>
      <li>Family Law</li><li>Divorce</li><li>Adoption</li><li>Annulment</li><li>Child Custody</li><li>Child Support</li><li>Cohabitation Agreements</li><li>Domestic Violence</li><li>Enforcement of Orders</li><li>Fathers' Rights</li><li>Grandparents' Rights</li><li>Legal Separation</li><li>Mediation</li>
    </ul>
  </aside>
</section>

<section class="testimonials">
  <h2 class="abs section-title" style="font-weight:700">Testimonials</h2>
  <div class="abs testi" style="left:102px">
    <div class="avatar" role="img" aria-label="Client portrait"></div><div class="quote-mark">“</div>
    <p class="quote">Pellentesque et pulvinar enim. Quisque at tempor ligula. Donec ut purus sed tortor malesuada.</p>
    <div class="t-name">Davin Holt</div><div class="t-role">Art Director / <b>lorem ipsum</b></div>
  </div>
  <div class="abs testi" style="left:447px">
    <div class="avatar" role="img" aria-label="Client portrait"></div><div class="quote-mark">“</div>
    <p class="quote">Pellentesque et pulvinar enim. Quisque at tempor ligula. Donec ut purus sed tortor malesuada.</p>
    <div class="t-name">Davin Holt</div><div class="t-role">Art Director / <b>lorem ipsum</b></div>
  </div>
  <div class="abs testi" style="left:789px">
    <div class="avatar" role="img" aria-label="Client portrait"></div><div class="quote-mark">“</div>
    <p class="quote">Pellentesque et pulvinar enim. Quisque at tempor ligula. Donec ut purus sed tortor malesuada.</p>
    <div class="t-name">Davin Holt</div><div class="t-role">Art Director / <b>lorem ipsum</b></div>
  </div>
  <div class="abs t-dots"><span class="on"></span><span></span><span></span><span></span></div>
</section>

<section class="contact-band">
  <h2 class="abs section-title" style="left:102px;font-weight:700">Location of Areas of Practice</h2>
  <div class="abs map" role="img" aria-label="Street map of the office area"></div>
  <div class="abs map-card">
    <h4>Halvard</h4>
    <p><svg width="10" height="14" viewBox="0 0 10 14"><path d="M5 0a5 5 0 0 0-5 5c0 4 5 9 5 9s5-5 5-9a5 5 0 0 0-5-5zm0 7a2 2 0 1 1 0-4 2 2 0 0 1 0 4z" fill="#fff"/></svg><span>418 Larkspur Lane<br>Houston, Texas - USA</span></p>
    <p><svg width="12" height="12" viewBox="0 0 24 24"><path fill="#fff" d="M6.6 10.8a15 15 0 0 0 6.6 6.6l2.2-2.2a1 1 0 0 1 1-.25 11.4 11.4 0 0 0 3.6.57 1 1 0 0 1 1 1V20a1 1 0 0 1-1 1A17 17 0 0 1 3 4a1 1 0 0 1 1-1h3.5a1 1 0 0 1 1 1c0 1.25.2 2.45.57 3.57a1 1 0 0 1-.25 1z"/></svg><span>555.310.4482</span></p>
    <p><svg width="12" height="10" viewBox="0 0 12 10"><rect width="12" height="10" fill="#fff"/><path d="M0 0l6 5 6-5" stroke="#1b1d20" fill="none"/></svg><span>desk@halvardlaw.example</span></p>
  </div>

  <h2 class="abs section-title" style="left:785px;font-weight:700">Request A Consultation</h2>
  <div class="abs form-label" style="top:111px">Name</div>
  <div class="abs field" style="top:126px;height:35px"></div>
  <div class="abs form-label" style="top:192px">Email</div>
  <div class="abs field" style="top:207px;height:37px"></div>
  <div class="abs form-label" style="top:272px">Phone</div>
  <div class="abs field" style="top:288px;height:36px"></div>
  <div class="abs form-label" style="top:355px">Short note about your case</div>
  <div class="abs field" style="top:370px;height:116px"></div>
  <div class="abs btn-yellow submit">Submit</div>
</section>

<footer class="site-footer">
  <h4 class="abs f-head" style="left:102px;font-weight:400">Useful links</h4>
  <ul class="abs f-links" style="left:102px"><li>Lorem ipsum dolor sit</li><li>amet, consectetu</li><li>dipiscing elit. Proin tincidunt</li><li>ullamcorper velit</li><li>et euismod dui ornare</li></ul>

  <h4 class="abs f-head" style="left:384px;font-weight:400">Friend Wall</h4>
  <div class="abs thumb" style="left:384px;top:98px" role="img" aria-label="Follower portrait"></div>
  <div class="abs thumb" style="left:455px;top:98px" role="img" aria-label="Follower portrait"></div>
  <div class="abs thumb" style="left:526px;top:98px" role="img" aria-label="Follower portrait"></div>
  <div class="abs thumb" style="left:384px;top:165px" role="img" aria-label="Follower portrait"></div>
  <div class="abs thumb" style="left:455px;top:165px" role="img" aria-label="Follower portrait"></div>
  <div class="abs thumb" style="left:526px;top:165px" role="img" aria-label="Follower portrait"></div>

  <h4 class="abs f-head" style="left:668px;font-weight:400">Latest news</h4>
  <ul class="abs f-links" style="left:668px"><li>Solace of a lonely highway</li><li>Write with purpose</li><li>Tree on a lake</li><li>Don't stop questioning</li><li>Overheard this morning</li></ul>

  <h4 class="abs f-head" style="left:954px;font-weight:400">Contact</h4>
  <div class="abs f-contact">
    <p><svg width="9" height="12" viewBox="0 0 10 14"><path d="M5 0a5 5 0 0 0-5 5c0 4 5 9 5 9s5-5 5-9a5 5 0 0 0-5-5z" fill="#8a8a8a"/></svg><span>418 Larkspur Lane<br>Houston, Texas - USA</span></p>
    <p><svg width="10" height="10" viewBox="0 0 24 24"><path fill="#8a8a8a" d="M6.6 10.8a15 15 0 0 0 6.6 6.6l2.2-2.2a1 1 0 0 1 1-.25 11.4 11.4 0 0 0 3.6.57 1 1 0 0 1 1 1V20a1 1 0 0 1-1 1A17 17 0 0 1 3 4a1 1 0 0 1 1-1h3.5a1 1 0 0 1 1 1c0 1.25.2 2.45.57 3.57a1 1 0 0 1-.25 1z"/></svg><span>555.310.4482</span></p>
    <p><svg width="11" height="9" viewBox="0 0 12 10"><rect width="12" height="10" fill="#8a8a8a"/></svg><span>contact@halvardlaw.example</span></p>
  </div>

  <div class="abs social" style="left:513px"></div>
  <div class="abs social" style="left:557px"></div>
  <div class="abs social" style="left:601px"></div>
  <div class="abs social" style="left:645px"></div>
  <div class="abs social" style="left:689px"></div>
  <div class="abs copy">Copyright © 2014 <b>Lorem ipsum dolor</b> / All rights reserved.</div>
</footer>
<div class="dash"></div>

</body>
</html>
```